ROAM Kelvara
Ease In, You've Arrived!
Bright & Fun-filled
Mina Pollard
PO Box 82
Tarrow Bay, Kelvara Island 2047
mina@roamkelvara.com
www.roamkelvara.com
Foot prints in sand

```html
<!DOCTYPE html>
<html lang="en">
<head>
<meta charset="utf-8">
<title>ROAM Kelvara – Business Card</title>
<link href="https://fonts.googleapis.com/css2?family=Source+Sans+3:wght@400;600&display=swap" rel="stylesheet">
<style>
  :root {
    --page-bg: #e9dcc9;
    --card-bg: #ffffff;
    --brand-blue: #1f8fd0;
    --brand-blue-deep: #1575b8;
    --brand-green: #8cc63f;
    --text-grey: #7a7a7a;
  }
  html, body {
    margin: 0;
    width: 1200px;
    height: 935px;
    overflow: hidden;
    background: var(--page-bg);
    font-family: "Source Sans 3", sans-serif;
  }
  .business-card {
    position: absolute;
    left: 192px;
    top: 233px;
    width: 815px;
    height: 468px;
    background: var(--card-bg);
    border-radius: 34px;
    overflow: hidden;
  }
  .brand {
    position: absolute;
    left: 88px;
    top: 112px;
    width: 340px;
  }
  .brand-row {
    display: flex;
    align-items: center;
    gap: 12px;
    white-space: nowrap;
  }
  .brand-dot {
    width: 34px;
    height: 34px;
    border-radius: 50%;
    background: var(--brand-green);
    flex: none;
  }
  .brand-name {
    font-size: 44px;
    font-weight: 600;
    color: var(--brand-blue);
    line-height: 1;
    letter-spacing: -0.5px;
  }
  .tagline {
    margin: 14px 0 0 46px;
    font-size: 20px;
    color: var(--brand-blue-deep);
    white-space: nowrap;
  }
  .contact {
    position: absolute;
    left: 483px;
    top: 108px;
    color: var(--text-grey);
    font-size: 22px;
    line-height: 28px;
    white-space: nowrap;
  }
  .contact-name {
    margin: 0 0 28px;
    font-size: 27px;
    line-height: 34px;
    font-weight: 600;
    color: var(--brand-green);
  }
  .contact p { margin: 0; }
  .label {
    color: var(--brand-green);
    font-weight: 600;
  }
  .waves {
    position: absolute;
    left: 0;
    bottom: 0;
    width: 815px;
    height: 100px;
  }
</style>
</head>
<body>
  <main class="business-card">
    <div class="brand">
      <div class="brand-row">
        <span class="brand-dot"></span>
        <span class="brand-name">ROAM Kelvara</span>
      </div>
      <p class="tagline">Ease In, You've Arrived!</p>
    </div>

    <section class="contact">
      <h1 class="contact-name">Mina Pollard</h1>
      <p>PO Box 82</p>
      <p>Tarrow Bay, Kelvara Island 2047</p>
      <p><span class="label">Phone :</span> 64 21 555 04 19</p>
      <p><span class="label">Email :</span> mina@roamkelvara.com</p>
      <p><span class="label">Web :</span> www.roamkelvara.com</p>
    </section>

    <svg class="waves" viewBox="0 0 815 100" preserveAspectRatio="none" aria-hidden="true">
      <defs>
        <linearGradient id="blueBand" x1="0" y1="0" x2="1" y2="0">
          <stop offset="0" stop-color="#1575b8"/>
          <stop offset="0.5" stop-color="#2aa3e0"/>
          <stop offset="1" stop-color="#1575b8"/>
        </linearGradient>
      </defs>
      <path d="M0 22 C 180 36, 330 52, 495 34 S 720 2, 815 6 L 815 22 C 720 18, 620 34, 495 48 S 200 46, 0 34 Z" fill="#8cc63f"/>
      <path d="M0 50 C 200 62, 340 80, 505 62 S 720 30, 815 32 L 815 100 L 0 100 Z" fill="url(#blueBand)"/>
    </svg>
  </main>
</body>
</html>
```